I need a new business card design for my pharmacy.

I need a business card design. I will include my logo.
The card needs to be readable. I prefer to have my logo on one side along with my website, the other side includes the other information. Please use combination of black, neon green, white, and silver. This needs to catch the eye but yet be clearly visible and legible. Thanks

Industry/Entity Type

Pharmacy

Contact Information for Business Card

It needs to have the following information listed:
Mel's Apothecary Owner/Pharm D.
7134 North Brook Lane
Sioux Falls, SD 57231
Phone 605-318-6207
Fax 605-318-6209
email: mel@melsapothecary-example.com
www.melsapothecary-example.com
Store hours Monday-Friday 8 am- 7 pm
Saturday 8 am- 12 pm
Sunday Closed
Please utilize the colors black, white, and neon green, maybe silver.

Requirements
Must have
• It needs to be easily readable!
Nice to have
• It should catch the eye.
Should not have
• Do not use any other colors except listed: black, neon green, white, & silver.

```html
<!DOCTYPE html>
<html lang="en">
<head>
<meta charset="utf-8">
<title>Mel's Apothecary – Business Card</title>
<link rel="stylesheet" href="https://fonts.googleapis.com/css2?family=Open+Sans:wght@400;600;700&display=swap">
<style>
  :root {
    --ink: #1d1d1f;
    --band: #232325;
    --neon: #a6d13a;
    --paper: #ffffff;
    --silver: #c4c6c8;
    --stage: #2a2a2c;
  }
  * { box-sizing: border-box; margin: 0; padding: 0; }
  html, body { width: 1200px; height: 750px; overflow: hidden; }
  body {
    background: var(--stage);
    font-family: "Open Sans", Arial, sans-serif;
    color: var(--ink);
    display: flex;
    align-items: center;
    justify-content: center;
    gap: 40px;
  }
  .card {
    position: relative;
    width: 540px;
    height: 309px;
    overflow: hidden;
  }

  /* Front: green */
  .card--front { background: var(--neon); }
  .front__brand {
    position: absolute;
    left: 92px; top: 88px;
    display: flex; align-items: center; gap: 14px;
  }
  .brand__dot {
    width: 26px; height: 26px; border-radius: 50%;
    background: var(--ink);
  }
  .brand__name {
    font-weight: 700;
    font-size: 36px;
    letter-spacing: -1.2px;
    color: var(--ink);
  }
  .front__rule {
    position: absolute;
    left: 40px; right: 40px; top: 188px;
    height: 1.5px; background: var(--ink);
  }
  .front__web {
    position: absolute; right: 40px; top: 164px;
    font-size: 12px;
  }
  .front__closed {
    position: absolute; right: 40px; top: 196px;
    font-size: 12px;
  }
  .hours {
    position: absolute; left: 40px; top: 214px;
    font-size: 13px; line-height: 1.35;
  }
  .hours__title { font-weight: 700; }
  .hours__row { display: flex; }
  .hours__day { width: 92px; }

  /* Back: white */
  .card--back { background: var(--paper); }
  .back__brand {
    position: absolute; left: 40px; top: 50px;
    display: flex; align-items: center; gap: 12px;
  }
  .back__brand .brand__dot { width: 20px; height: 20px; background: var(--neon); }
  .back__brand .brand__name { font-size: 28px; }
  .band {
    position: absolute; left: 0; right: 0; top: 118px;
    height: 58px; background: var(--band);
  }
  .band__title {
    position: absolute; left: 40px; top: 6px;
    color: var(--neon); font-weight: 700; font-size: 18px;
  }
  .band__role {
    position: absolute; left: 40px; top: 32px;
    color: var(--neon); font-size: 13px;
  }
  .band__mark {
    position: absolute; right: 52px; top: -22px;
    width: 100px; height: 100px; border-radius: 50%;
    background: var(--paper);
    border: 6px solid var(--silver);
  }
  .contacts {
    position: absolute; left: 40px; bottom: 34px;
    list-style: none; font-size: 13px; line-height: 1.6;
  }
  .contacts li { display: flex; align-items: center; gap: 8px; }
  .contacts svg { width: 13px; height: 13px; fill: var(--ink); }
  .address {
    position: absolute; right: 40px; top: 200px;
    font-style: normal; font-size: 13px; line-height: 1.5; text-align: right;
  }
</style>
</head>
<body>
  <section class="card card--front" aria-label="Card front">
    <div class="front__brand">
      <span class="brand__dot"></span>
      <span class="brand__name">Mel's Apothecary</span>
    </div>
    <p class="front__web">www.melsapothecary-example.com</p>
    <div class="front__rule"></div>
    <p class="front__closed">Sunday Closed</p>
    <div class="hours">
      <p class="hours__title">STORE HOURS</p>
      <p class="hours__row"><span class="hours__day">Mon to Fri</span><span>: 8 am - 7 pm</span></p>
      <p class="hours__row"><span class="hours__day">Saturday</span><span>: 8 am - 12 pm</span></p>
    </div>
  </section>

  <section class="card card--back" aria-label="Card back">
    <div class="back__brand">
      <span class="brand__dot"></span>
      <span class="brand__name">Mel's Apothecary</span>
    </div>
    <div class="band">
      <p class="band__title">Pharm D.</p>
      <p class="band__role">Owner</p>
      <span class="band__mark"></span>
    </div>
    <ul class="contacts">
      <li><svg viewBox="0 0 16 16"><path d="M3 1h3l1.5 4-2 1.2a8 8 0 0 0 4.3 4.3L11 8.5l4 1.5v3a2 2 0 0 1-2 2A12 12 0 0 1 1 3a2 2 0 0 1 2-2z"/></svg>605-318-6207</li>
      <li><svg viewBox="0 0 16 16"><path d="M4 1h7v4H4zM2 6h12v7h-2v2H4v-2H2zm3 4v4h6v-4z"/></svg>605-318-6209</li>
      <li><svg viewBox="0 0 16 16"><path d="M1 3h14v10H1zm1.5 1.2V5l5.5 4 5.5-4v-.8L8 8z"/></svg>mel@melsapothecary-example.com</li>
    </ul>
    <address class="address">
      7134 North Brook Lane<br>
      Sioux Falls, SD 57231<br>
      www.melsapothecary-example.com
    </address>
  </section>
</body>
</html>
```